Information Technology Company needs a Website...

We need a single page website for new technology company called:

MERIVALE CREST TECHNOLOGY GROUP
Based in Ojai CA.

We are offering three primary services:

- Business Solutions

- IT Services

- Software Implementation and Consulting

We want a single page design where all content scrolls down/up on one page. We're looking for the following characteristics:

- Home/Landing
- Active background with panoramic view (Will provide content)

- Business Solutions, IT Services, Software Implementation and Consulting

List of software vendors we recommend (Company logos)

- About
- History
- Our Team
- Partners

I'll upload our new logo as soon as we get the design files. I'll also send over some example website layout's that we like shortly.

Target Market(s)

Small/Medium Businesses

Industry/Entity Type

Information Technology

Number of Pages Required

1 page

Font styles to use
Other font styles liked:
• Sansation

Requirements
Must have
• Full page browser width, easy navigation and visibility. Creative design, not like every other "Technology" website template. Should be the "One Page" design where each section is below the next and the user scrolls down the page through the whole site. I like the concept of the following website in the main "Whiteboard" image:
• http://www.plinkoria-sample.com/design/4082913
• And the way this site does the active panoramic background:
• http://www.vantrelwork-sample.com/
• Something interesting and appealing to potential clients looking for Small/Medium business solutions and IT Services.
• Use uploaded Logo to establish color and theme for website.
Should not have
• Look the same as every other information technology website template.

```html
<!DOCTYPE html>
<html lang="en">
<head>
<meta charset="utf-8">
<title>Merivale Crest Technology Group</title>
<link href="https://fonts.googleapis.com/css2?family=Maven+Pro:wght@400;500;700&display=swap" rel="stylesheet">
<style>
:root{
  --accent:#e8471f;
  --ink:#333333;
  --muted:#7a7a7a;
  --soft:#f2f2f2;
  --panel:#e4e4e4;
  --dark:#2b2b2b;
  --darker:#222222;
  --white:#ffffff;
  --line:#d4d4d4;
}
*{box-sizing:border-box;margin:0;padding:0}
html,body{width:1200px;height:2203px;overflow:hidden}
body{font-family:"Maven Pro",Arial,sans-serif;color:var(--ink);position:relative;
  background:linear-gradient(180deg,#bfe0ec 0%,#8fbfd1 14%,#6d7f86 22%,#3d3f3f 40%,#a9d3e2 42%,#8cb7c6 58%,#3b3d3d 68%,#b4dae7 70%,#4a4f50 92%,#3a3d3d 100%)}
.backdrop{position:absolute;inset:0}
.page{position:absolute;left:187px;top:0;width:826px;height:2203px;background:var(--white)}
section,header,footer{position:relative;width:826px}

/* header */
.site-header{height:95px;display:flex;align-items:center;justify-content:space-between;padding:0 12px 0 12px}
.brand{color:#4a4a4a;font-weight:700;line-height:1}
.brand-name{font-size:27px;letter-spacing:-.5px;display:block}
.brand-sub{font-size:10.5px;letter-spacing:2.2px;display:block;margin-top:5px}
.nav{display:flex;gap:22px;font-size:10.5px;font-weight:700;text-transform:uppercase}
.nav a{color:var(--ink);text-decoration:none}
.nav a.active{color:var(--accent)}

/* hero */
.hero{height:353px;background:radial-gradient(ellipse 18% 55% at 50% 38%,#dbe9f2 0%,#8fb5cf 35%,transparent 70%),linear-gradient(180deg,#3a3a3a,#2a2a2a 60%,#393939)}
.hero-arrow{position:absolute;top:176px;width:14px;height:14px;stroke:#ddd;fill:none;stroke-width:2}
.hero-arrow.prev{left:8px}.hero-arrow.next{right:8px}

/* services */
.services{height:286px;text-align:center}
.section-lead{font-size:15px;font-weight:500;text-transform:uppercase;padding-top:42px}
.service-grid{display:flex;justify-content:space-between;padding:0 12px;margin-top:32px}
.service{width:260px;height:150px;position:relative}
.service svg{width:34px;height:34px}
.service h3{color:var(--accent);font-size:15px;font-weight:700;text-transform:uppercase;margin-top:8px;line-height:1.05;height:32px;display:flex;align-items:center;justify-content:center}
.service p{font-size:8.5px;color:#666;line-height:1.5;margin-top:6px}
.btn-outline{position:absolute;left:50%;bottom:0;transform:translateX(-50%);width:70px;height:28px;border:1px solid #bbb;font-size:8.5px;line-height:26px;color:#555}

/* about */
.about{height:213px;background:var(--soft);padding:22px 12px}
.about h2{color:var(--accent);font-size:24px;font-weight:700}
.about p{width:565px;font-size:11px;line-height:1.65;color:#555;margin-top:4px}
.btn-dark{display:inline-block;background:#3b3b3b;color:var(--white);font-size:9.5px;padding:8px 12px;margin-top:10px}
.about-photo{position:absolute;right:15px;top:15px;width:219px;height:184px;background:linear-gradient(135deg,#dfe9f3 0%,#93aecd 45%,#3a4a63 75%,#c8d6e6 100%)}

/* history */
.history{height:493px}
.history h2,.team h2{text-align:center;color:var(--accent);font-size:24px;font-weight:700;padding-top:35px}
.timeline-line{position:absolute;left:410px;top:81px;width:4px;height:375px;background:#ddd}
.event{position:absolute;width:826px;height:50px}
.event .year{position:absolute;top:-4px;color:var(--accent);font-size:15px}
.event .flag{position:absolute;top:0;width:16px;height:12px}
.event .body{position:absolute;top:0;width:370px}
.event h4{font-size:10.5px;font-weight:500;color:#222}
.event p{font-size:8.5px;color:#888;line-height:1.55;margin-top:3px}
.event.right .year{right:440px}
.event.right .flag{left:404px}
.event.right .body{left:438px}
.event.left .year{left:438px}
.event.left .flag{left:404px;transform:scaleX(-1)}
.event.left .body{right:440px;text-align:right}

/* team */
.team{height:257px;background:var(--soft)}
.team-row{position:absolute;top:83px;left:0;width:826px}
.member{position:absolute;width:140px;margin-left:-70px;text-align:center}
.member .portrait{width:88px;height:88px;margin:0 auto;background:linear-gradient(180deg,#e9e9e9 0%,#cfcfcf 55%,#2e2e2e 100%)}
.member h4{font-size:12px;font-weight:500;margin-top:10px;color:#222}
.member p{font-size:8.5px;color:#888;line-height:1.4;margin-top:4px}

/* partners */
.partners{height:132px;text-align:center}
.partners h2{color:#9b9b9b;font-size:22px;font-weight:500;padding-top:36px;letter-spacing:.5px}
.partner-row{display:flex;justify-content:space-between;padding:0 22px;margin-top:14px}
.partner{font-size:15px;font-weight:500;color:#555}

/* contact */
.contact{height:217px;display:flex}
.map{width:413px;height:217px;background:radial-gradient(ellipse at 40% 45%,#e6e6e6,#c9c9c9 60%,#b8b8b8)}
.contact-panel{flex:1;background:var(--panel);padding:20px 0 0 42px}
.contact-panel h3{font-size:20px;font-weight:400;color:#222}
.form{display:grid;grid-template-columns:161px 161px;gap:11px 8px;margin-top:14px}
.field{height:32px;background:var(--white);font-size:9.5px;color:#555;padding:10px 14px}
.submit{height:32px;background:var(--darker);color:var(--white);font-size:10px;text-align:center;line-height:32px;text-transform:uppercase}

/* footer */
.site-footer{height:157px;background:var(--dark);color:#bbb;font-size:9.5px}
.info-row{display:flex;justify-content:space-between;padding:38px 28px 0 15px}
.info-row span{display:flex;align-items:center;gap:6px}
.info-row svg{width:10px;height:10px;fill:#bbb}
.rule{position:absolute;left:0;top:83px;width:826px;height:1px;background:#3b3b3b}
.footer-links{position:absolute;left:15px;top:107px;font-size:8.5px}
.copyright{position:absolute;left:15px;top:132px;font-size:8.5px}
.social{position:absolute;right:28px;top:115px;display:flex;gap:6px}
.social i{display:block;width:21px;height:21px;border-radius:50%}
.social i:nth-child(1){background:#3b5998}.social i:nth-child(2){background:#2fa3dd}
.social i:nth-child(3){background:#1f7bb6}.social i:nth-child(4){background:#d93f2c}
</style>
</head>
<body>
<div class="backdrop" role="img" aria-label="Panoramic city skyline with towers under a pale sky"></div>
<div class="page">

<header class="site-header">
  <div class="brand"><span class="brand-name">merivale crest</span><span class="brand-sub">TECHNOLOGY GROUP</span></div>
  <nav class="nav"><a class="active" href="#">Home</a><a href="#">About us</a><a href="#">History</a><a href="#">Our team</a><a href="#">Partners</a><a href="#">Contact us</a></nav>
</header>

<section class="hero" role="img" aria-label="Businessman facing a road arrow rising into a bright sky, chalkboard sketches of SEO, branding and business growth around him">
  <svg class="hero-arrow prev" viewBox="0 0 14 14"><path d="M9 2 4 7l5 5"/></svg>
  <svg class="hero-arrow next" viewBox="0 0 14 14"><path d="M5 2l5 5-5 5"/></svg>
</section>

<section class="services">
  <h2 class="section-lead">We are offering three primary services</h2>
  <div class="service-grid">
    <div class="service">
      <svg viewBox="0 0 34 34"><rect x="3" y="10" width="28" height="19" rx="2" fill="#e8471f"/><rect x="12" y="5" width="10" height="6" rx="1" fill="none" stroke="#e8471f" stroke-width="2.4"/><rect x="3" y="17" width="28" height="2" fill="#fff"/><rect x="15" y="15" width="4" height="5" fill="#e8471f"/></svg>
      <h3>Business solutions</h3>
      <p>Nunc sit amet urna auctor, vestibulum nibh id, volutpat neque. Vestibulum ante ipsum primis in faucibus orci luctus et ultrices posuere cubilia Curae; Duis a odio pharetra.</p>
      <span class="btn-outline">Read more</span>
    </div>
    <div class="service">
      <svg viewBox="0 0 34 34"><rect x="3" y="6" width="28" height="19" rx="2" fill="none" stroke="#e8471f" stroke-width="2.6"/><rect x="14" y="25" width="6" height="4" fill="#e8471f"/><rect x="10" y="29" width="14" height="2.5" fill="#e8471f"/></svg>
      <h3>IT services</h3>
      <p>Nunc sit amet urna auctor, vestibulum nibh id, volutpat neque. Vestibulum ante ipsum primis in faucibus orci luctus et ultrices posuere cubilia Curae; Duis a odio pharetra.</p>
      <span class="btn-outline">Read more</span>
    </div>
    <div class="service">
      <svg viewBox="0 0 34 34"><rect x="2" y="8" width="30" height="18" rx="2" fill="none" stroke="#e8471f" stroke-width="2.4"/><g fill="#e8471f"><rect x="6" y="12" width="3" height="3"/><rect x="11" y="12" width="3" height="3"/><rect x="16" y="12" width="3" height="3"/><rect x="21" y="12" width="3" height="3"/><rect x="26" y="12" width="3" height="3"/><rect x="6" y="17" width="3" height="3"/><rect x="11" y="17" width="3" height="3"/><rect x="16" y="17" width="3" height="3"/><rect x="21" y="17" width="3" height="3"/><rect x="26" y="17" width="3" height="3"/><rect x="10" y="21.5" width="14" height="2.5"/></g></svg>
      <h3>Software implementation and consulting</h3>
      <p>Nunc sit amet urna auctor, vestibulum nibh id, volutpat neque. Vestibulum ante ipsum primis in faucibus.</p>
      <span class="btn-outline">Read more</span>
    </div>
  </div>
</section>

<section class="about">
  <h2>ABOUT US</h2>
  <p>Curabitur eget viverra tortor. Pellentesque cursus ligula ultricies hendrerit porta. In aliquam condimentum dui. Vivamus rhoncus, libero eu suscipit condimentum, nibh libero finibus quam, ac vestibulum nibh eros id massa. In fermentum nisl nec est luctus, a accumsan libero fermentum. Fusce et lorem in ipsum varius congue nec ut lacus. Nunc sit amet urna auctor, vestibulum nibh id, volutpat neque. Morbi scelerisque nec ipsum eu suscipit. Cras viverra elit vitae congue interdum. Aliquam hendrerit, tortor nec molestie fermentum</p>
  <span class="btn-dark">Contact Us</span>
  <div class="about-photo" role="img" aria-label="Hands working on a laptop at an office desk"></div>
</section>

<section class="history">
  <h2>HISTORY</h2>
  <div class="timeline-line"></div>
  <svg width="0" height="0" style="position:absolute"><defs><symbol id="flag" viewBox="0 0 16 12"><path d="M0 0h11l5 6-5 6H0z" fill="#e8471f"/></symbol></defs></svg>

  <div class="event right" style="top:103px"><span class="year">2000</span><svg class="flag"><use href="#flag"/></svg>
    <div class="body"><h4>Curabitur eget</h4><p>Pellentesque cursus ligula ultricies hendrerit porta. In aliquam condimentum dui. Vivamus rhoncus, libero eu suscipit condimentum, nibh libero finibus quam.</p></div></div>

  <div class="event left" style="top:177px"><span class="year">2004</span><svg class="flag"><use href="#flag"/></svg>
    <div class="body"><h4>Morbi in felis a massa</h4><p>Pellentesque cursus ligula ultricies hendrerit porta. In aliquam condimentum dui. Vivamus rhoncus, libero eu suscipit condimentum, nibh libero finibus quam.</p></div></div>

  <div class="event right" style="top:250px"><span class="year">2008</span><svg class="flag"><use href="#flag"/></svg>
    <div class="body"><h4>Aliquam scelerisque dolor</h4><p>Pellentesque cursus ligula ultricies hendrerit porta. In aliquam condimentum dui. Vivamus rhoncus, libero eu suscipit condimentum, nibh libero finibus quam.</p></div></div>

  <div class="event left" style="top:324px"><span class="year">2012</span><svg class="flag"><use href="#flag"/></svg>
    <div class="body"><h4>Nunc sit amet urna auctor</h4><p>Pellentesque cursus ligula ultricies hendrerit porta. In aliquam condimentum dui. Vivamus rhoncus, libero eu suscipit condimentum, nibh libero finibus quam.</p></div></div>

  <div class="event right" style="top:397px"><span class="year">2016</span><svg class="flag"><use href="#flag"/></svg>
    <div class="body"><h4>Cras viverra elit vitae</h4><p>Pellentesque cursus ligula ultricies hendrerit porta. In aliquam condimentum dui. Vivamus rhoncus, libero eu suscipit condimentum, nibh libero finibus quam.</p></div></div>
</section>

<section class="team">
  <h2>OUR TEAM</h2>
  <div class="team-row">
    <div class="member" style="left:79px"><div class="portrait" role="img" aria-label="Portrait of a team member"></div><h4>Alex Marlow</h4><p>Pellentesque cursus<br>ligula ultricies</p></div>
    <div class="member" style="left:246px"><div class="portrait" role="img" aria-label="Portrait of a team member"></div><h4>Alex Marlow</h4><p>Pellentesque cursus<br>ligula ultricies</p></div>
    <div class="member" style="left:412px"><div class="portrait" role="img" aria-label="Portrait of a team member"></div><h4>Alex Marlow</h4><p>Pellentesque cursus<br>ligula ultricies</p></div>
    <div class="member" style="left:579px"><div class="portrait" role="img" aria-label="Portrait of a team member"></div><h4>Alex Marlow</h4><p>Pellentesque cursus<br>ligula ultricies</p></div>
    <div class="member" style="left:746px"><div class="portrait" role="img" aria-label="Portrait of a team member"></div><h4>Alex Marlow</h4><p>Pellentesque cursus<br>ligula ultricies</p></div>
  </div>
</section>

<section class="partners">
  <h2>PARTNERS</h2>
  <div class="partner-row">
    <span class="partner">Fernbrook</span><span class="partner">Quillon</span><span class="partner">Larkvane</span><span class="partner">Tovi</span>
    <span class="partner">Brenmark</span><span class="partner">Halvo</span><span class="partner">Oristel</span><span class="partner">Nuvara</span>
  </div>
</section>

<section class="contact">
  <div class="map" role="img" aria-label="Grey world map"></div>
  <div class="contact-panel">
    <h3>Contact us</h3>
    <div class="form">
      <div class="field">Name</div><div class="field">Company</div>
      <div class="field">Phone</div><div class="field">Email</div>
      <div class="field">Message</div><div class="submit">Submit</div>
    </div>
  </div>
</section>

<footer class="site-footer">
  <div class="info-row">
    <span><svg viewBox="0 0 10 10"><path d="M5 0a3.5 3.5 0 0 0-3.5 3.5C1.5 6 5 10 5 10s3.5-4 3.5-6.5A3.5 3.5 0 0 0 5 0zm0 5a1.5 1.5 0 1 1 0-3 1.5 1.5 0 0 1 0 3z"/></svg>24 Building name, Street name City - Zipcode</span>
    <span><svg viewBox="0 0 10 10"><path d="M2 0l2 2.5-1 1.2a6 6 0 0 0 3.3 3.3l1.2-1L10 8 8.5 10C4 9.5.5 6 0 1.5z"/></svg>Call Now: 805 410 2276</span>
    <span><svg viewBox="0 0 10 10"><rect x="1" y="3" width="8" height="6"/><rect x="3" y="0" width="4" height="3"/></svg>Fax : 805 410 2277</span>
    <span><svg viewBox="0 0 10 10"><path d="M0 2h10v6H0z"/></svg>Email: info@merivalecrestconsulting.com</span>
  </div>
  <div class="rule"></div>
  <div class="footer-links">Home | About us | History | Our Team | Partners | Contact us</div>
  <div class="copyright">Copyright © 2016 Merivale Crest Consulting. All rights reserved.</div>
  <div class="social"><i></i><i></i><i></i><i></i></div>
</footer>

</div>
</body>
</html>
```